Learning platform for primary and secondary schools needs a new design

We need to restyle the website: www.pennaboschetto.org.
We are developing new functionalities that will enable to turn the platform in an interactive e-learning center for teachers, parents and pupils. Our target is providing contents and learning methods for primary and secondary school.
We want to give a new structure to the homepage and all menu sections and to find a new design that facilitates users to orientate themselves. We love our main picture and we would like to emphasize it. We like our logo and we don't want to change it.
The homepage should fulfil three main tasks:
- welcome visitors;
- encourage visitors to explore three areas of free contents: learning (scopri), experimenting (esperimenti), cooking (ricette)
- convert visitors in logged users (users can register as teachers, parents or students).
We also need a new design for:
- log-in page,
- slideshow,
- galleries of pictures,
- blog page,
- newsletter.
If you have any questions, do not hesitate to contact me.
Good job!
Giulia
Updates
Hi guys,
First of all I'd like to say thanks to all designers that submitted their ideas.
Up to now I didn't find any design that really convinced me, that's why I decided to share with you a design idea that could make easier your job (please see again the project briefing). I can't wait to see your new designs!
Good job
Ciao
Giuliabetta
Hi guys,
I would like to thank you for all your wonderful design proposals. We have just launched a friends and family voting pool to help us in getting the final decision. We'll let you know the result as soon as possible within tomorrow.
Ciao
Giuliabetta
Target Market(s)
Italian teachers, parents and students attending primary and secondary school
Industry/Entity Type
Cooking
Look and feel
Each slider illustrates characteristics of the customer's brand and the style your logo design should communicate.

```html
<!DOCTYPE html>
<html lang="it">
<head>
<meta charset="utf-8">
<title>PennaBoschetto</title>
<link href="https://fonts.googleapis.com/css2?family=Bree+Serif&family=Delius&family=Sniglet:wght@400&family=Open+Sans:wght@400;600;700&family=Noto+Serif:ital,wght@0,700;1,400;1,700&display=swap" rel="stylesheet">
<style>
:root{
  --sky-top:#2e9bbd;--sky-mid:#5fbcd6;--sky-low:#a9dceb;
  --sand:#eedcae;--white:#ffffff;
  --teal:#2a8a98;--teal-btn:#5db5d2;--nav-btn:#7ecbe2;--nav-active:#4aa82c;
  --orange:#f07a1a;--brown:#8b4a12;--green:#7dba2c;--green-dark:#5f9e1c;
  --text:#6f6f6f;--title:#333;--grey-box:#ededed;--dash:#c9c9c9;
  --footer:#0c2a37;--footer-text:#d8e3e8;
}
*{margin:0;padding:0;box-sizing:border-box}
html,body{width:813px;height:1200px;overflow:hidden}
body{position:relative;background:var(--white);font-family:"Open Sans",sans-serif;color:var(--text)}
.abs{position:absolute}
.hero-bg{left:0;top:0;width:813px;height:470px;
  background:linear-gradient(180deg,var(--sky-top) 0,var(--sky-mid) 190px,var(--sky-low) 400px,var(--sand) 410px,#f6ecd0 440px,var(--white) 470px)}
.ground{left:0;top:402px;width:813px;height:9px;background:linear-gradient(180deg,#8cc44a,#c9d97a)}
.logo{left:72px;top:60px;display:flex;align-items:center;gap:6px;font-weight:700;font-size:16px;color:var(--orange)}
.logo i{width:22px;height:22px;border-radius:50%;background:#fff;display:block}
.search{left:594px;top:19px;width:145px;height:21px;background:var(--nav-btn);border-radius:2px;font:italic 9px "Open Sans",sans-serif;color:#e8f6fb;padding:5px 8px}
.search svg{position:absolute;right:6px;top:4px}
.social{top:50px;width:22px;height:22px;border-radius:50%;background:#1d7fa2}
.nav{left:0;top:88px}
.nav a{position:absolute;top:0;height:21px;background:var(--nav-btn);color:#fff;font-size:9.5px;font-weight:600;text-decoration:none;text-align:center;line-height:21px;border-radius:2px}
.nav a.active{background:var(--nav-active)}
.hero-title{left:0;width:813px;top:136px;text-align:center;font:21px "Bree Serif",serif;color:#fff;text-shadow:0 1px 2px rgba(0,0,0,.2)}
.hero-sub{left:0;width:813px;top:170px;text-align:center;font:13px/19px "Delius",cursive;color:#fff}
.town{left:168px;top:224px;width:476px;height:216px;border-radius:6px;background:linear-gradient(180deg,#e2874a,#f0b24e 50%,#6bb3a6)}
.welcome{left:0;width:813px;top:468px;text-align:center;font:21px "Bree Serif",serif;color:var(--brown)}
.intro{left:96px;width:620px;top:509px;text-align:center;font-size:10.4px;line-height:16.2px}
.dash{height:0;border-top:1px dashed var(--dash)}
.btn{height:24px;border:2px solid var(--teal-btn);border-radius:4px;background:#fff;font-size:9px;font-weight:700;color:#222;display:flex;align-items:center;padding-left:10px;gap:8px;box-shadow:0 1px 2px rgba(0,0,0,.15);white-space:nowrap}
.btn .arrow{width:13px;height:13px;border-radius:50%;background:#e6eef1;display:flex;align-items:center;justify-content:center;flex:none}
.btn.orange{border-color:var(--orange)}
.btn.green{border-color:var(--green)}
.sec-title{font:400 19px "Sniglet",cursive;white-space:nowrap}
.teal{color:var(--teal)}.orangec{color:var(--orange)}.greenc{color:var(--green)}
.feature-img{width:66px;height:56px;border-radius:6px}
.feature h3{font-size:10.5px;font-weight:600;color:var(--title);margin-bottom:2px;white-space:nowrap}
.feature p{font-size:9px;line-height:13.6px;width:146px}
.viewall{font-size:9px;font-weight:600;color:var(--green)}
.small{font-size:9px;line-height:13.6px}
.email{left:535px;top:714px;width:140px;height:22px;background:#c9c9c9;border-radius:2px;font:italic 9px "Open Sans",sans-serif;color:#777;padding:5px 8px}
.subscribe{left:680px;top:714px;width:58px;height:22px;background:var(--teal-btn);color:#fff;font-size:9.5px;text-align:center;line-height:22px;border-radius:2px}
.price{left:535px;top:748px;width:203px;height:58px;border:1px solid #d5d5d5;border-radius:4px;background:#f6f6f6;overflow:hidden}
.price .tag{position:absolute;left:0;top:0;width:85px;height:58px;background:var(--teal-btn);color:#fff;text-align:center;font-size:11px;line-height:12px;padding-top:5px;clip-path:polygon(0 0,80px 0,85px 50%,80px 100%,0 100%)}
.price .tag b{display:block;font-size:20px;line-height:21px}
.price .info{position:absolute;left:108px;top:7px;font-size:11px;line-height:12px;color:#555}
.price .info span{display:block;margin-top:6px;color:var(--teal-btn);font-size:12px}
.bar{height:23px;color:#fff;font:400 13px/17px "Sniglet",cursive;padding:3px 9px;white-space:nowrap}
.bar.green{background:var(--green)}
.gallery-img{left:74px;top:940px;width:208px;height:90px;border:4px solid #e6e6e6;border-radius:4px;background:linear-gradient(180deg,#8ed0ea,#f0a855 55%,#e9dcb6)}
.thumb{left:302px;top:944px;width:53px;height:51px;border:3px solid #eee;background:linear-gradient(135deg,#f7d36a,#f08a2c)}
.date{font-size:8.5px;color:#999}
.post-title{font:700 9.5px/13.6px "Noto Serif",serif;color:var(--orange)}
.sep{height:1px;background:#e3e3e3}
.tweet{left:537px;width:201px;background:var(--grey-box);border-radius:4px;padding:6px 8px;font:italic 9.5px/13.6px "Noto Serif",serif;color:#999}
.tweet b{color:#777}
.tweet::before{content:"";position:absolute;left:-7px;top:26px;border:7px solid transparent;border-left:0;border-right-color:var(--grey-box)}
.footer{left:0;top:1137px;width:813px;height:63px;background:var(--footer);color:var(--footer-text);text-align:center;font-size:9px}
.footer .links{margin-top:17px}
.footer .links span{margin:0 7px}
.footer .copy{margin-top:8px}
</style>
</head>
<body>
<div class="abs hero-bg"></div>
<div class="abs ground"></div>

<div class="abs logo"><i></i>PennaBoschetto</div>

<div class="abs search">Search Here...
  <svg width="12" height="12" viewBox="0 0 12 12"><circle cx="5" cy="5" r="3.6" fill="none" stroke="#3c8aa8" stroke-width="1.6"/><line x1="7.6" y1="7.6" x2="11" y2="11" stroke="#3c8aa8" stroke-width="1.8"/></svg>
</div>
<div class="abs social" style="left:608px"></div>
<div class="abs social" style="left:636px"></div>
<div class="abs social" style="left:663px"></div>
<div class="abs social" style="left:690px"></div>
<div class="abs social" style="left:717px"></div>

<nav class="abs nav">
  <a class="active" style="left:240px;width:48px">HOME</a>
  <a style="left:294px;width:58px">SCOPRI</a>
  <a style="left:358px;width:82px">ESPERIMENTI</a>
  <a style="left:447px;width:57px">RICETTE</a>
  <a style="left:510px;width:57px">BLOG</a>
  <a style="left:574px;width:74px">GLOSSARIO</a>
  <a style="left:655px;width:83px">IL PROGETTO</a>
</nav>

<h1 class="abs hero-title">PennaBoschetto, il Gusto Della Conoscenza.</h1>
<p class="abs hero-sub">Il sito pennaboschetto è in aggiornamento.<br>Torna a trovarci il 3 settembre con nuovi contenuti e nuove funzionalità.</p>
<div class="abs town" role="img" aria-label="Illustrazione principale: una via di case colorate con botteghe di pane, latte, pesce e frutta"></div>

<h2 class="abs welcome">Welcome To PennaBoschetto.com</h2>
<p class="abs intro">Lorem ipsum dolor sit amet, consectetur adipisicing elit, sed do eiusmod tempor incididunt ut labore et dolore magna aliqua. Ut enim ad minim veniam, quis nostrud exercitation ullamco laboris nisi ut aliquip ex ea commodo consequat. Duis aute irure dolor in reprehenderit in voluptate velit esse cillum dolore eu fugiat nulla pariatur. Excepteur sint occaecat cupidatat non proident, sunt in culpa qui officia deserunt mollit anim id est laborum.</p>

<div class="abs dash" style="left:74px;top:602px;width:664px"></div>
<div class="abs btn" style="left:330px;top:590px;width:153px"><span class="arrow"><svg width="8" height="6" viewBox="0 0 8 6"><path d="M0 3h6M4 1l2 2-2 2" stroke="#3c8aa8" stroke-width="1.2" fill="none"/></svg></span>Read more about features</div>

<h2 class="abs sec-title teal" style="left:74px;top:628px">Encourage Visitors</h2>

<div class="abs feature-img" style="left:74px;top:684px;background:linear-gradient(160deg,#f3c23a,#e0572c 50%,#3b8fd0)" role="img" aria-label="Pila di libri colorati"></div>
<div class="abs feature" style="left:150px;top:673px"><h3>PennaBoschetto, Scopri</h3><p>Lorem ipsum dolor sit amet, consectetur adipisicing elit, sed do eiusmod tempor..</p><div class="viewall">→ View All</div></div>

<div class="abs feature-img" style="left:312px;top:666px;height:70px;background:linear-gradient(180deg,#f2f2f2,#cfcfcf)" role="img" aria-label="Disegno di un cuoco con mestolo"></div>
<div class="abs feature" style="left:379px;top:673px"><h3>PennaBoschetto, Esperimenti</h3><p>Lorem ipsum dolor sit amet, consectetur adipisicing elit, sed do eiusmod tempor..</p><div class="viewall">→ View All</div></div>

<div class="abs feature-img" style="left:74px;top:778px;background:linear-gradient(180deg,#a9d86a,#f5c88a)" role="img" aria-label="Disegno di due bambini con un vassoio"></div>
<div class="abs feature" style="left:150px;top:770px"><h3>PennaBoschetto, Ricette</h3><p>Lorem ipsum dolor sit amet, consectetur adipisicing elit, sed do eiusmod tempor..</p><div class="viewall">→ View All</div></div>

<div class="abs feature-img" style="left:312px;top:776px;width:58px;height:50px;background:linear-gradient(135deg,#f3ea5a,#ee8fb5)" role="img" aria-label="Foglietti adesivi con consigli"></div>
<div class="abs feature" style="left:379px;top:770px"><h3>PennaBoschetto</h3><p>Lorem ipsum dolor sit amet, consectetur adipisicing elit, sed do eiusmod tempor..</p><div class="viewall">→ View All</div></div>

<div class="abs btn" style="left:76px;top:852px;width:154px"><span class="arrow"><svg width="8" height="6" viewBox="0 0 8 6"><path d="M0 3h6M4 1l2 2-2 2" stroke="#3c8aa8" stroke-width="1.2" fill="none"/></svg></span>Read more about features</div>

<h2 class="abs sec-title orangec" style="left:535px;top:628px">Newsletter</h2>
<p class="abs small" style="left:535px;top:664px;width:205px">Lorem ipsum dolor sit amet, consectetur adipisicing elit, sed do eiusmod tempor incididunt ut labore et dolore magna aliqua.</p>
<div class="abs email">Email</div>
<div class="abs subscribe">Subcribe</div>
<div class="abs price"><div class="tag">From<b>£6.25</b>a month</div><div class="info">No contract<br>or joining fee<span>Learn more</span></div></div>
<p class="abs small" style="left:535px;top:814px;width:205px">Lorem ipsum dolor sit amet, consectetur adipisicing elit, sed do eiusmod tempor..</p>
<div class="abs btn orange" style="left:535px;top:851px;width:150px;font-size:8.5px"><span class="arrow"><svg width="8" height="6" viewBox="0 0 8 6"><path d="M0 3h6M4 1l2 2-2 2" stroke="#f07a1a" stroke-width="1.2" fill="none"/></svg></span>Sign up PennaBoschetto</div>

<div class="abs dash" style="left:74px;top:896px;width:208px"></div>
<div class="abs dash" style="left:302px;top:896px;width:209px"></div>
<div class="abs dash" style="left:530px;top:896px;width:208px"></div>

<h2 class="abs sec-title greenc" style="left:74px;top:906px;font-size:17px">PennaBoschetto Gallery</h2>
<div class="abs gallery-img" role="img" aria-label="Galleria: la via di case colorate con le botteghe"></div>
<p class="abs small" style="left:74px;top:1038px;width:210px">Lorem ipsum dolor sit amet, consectetur adipisicing elit, sed do eiusmod tempor incididunt ut labore et dolore magna aliqua.</p>
<div class="abs btn green" style="left:76px;top:1089px;width:78px"><span class="arrow"><svg width="8" height="6" viewBox="0 0 8 6"><path d="M0 3h6M4 1l2 2-2 2" stroke="#5f9e1c" stroke-width="1.2" fill="none"/></svg></span>View All</div>

<div class="abs bar green" style="left:302px;top:907px;width:209px">Our Blog</div>
<div class="abs thumb" role="img" aria-label="Miniatura dell'articolo"></div>
<div class="abs" style="left:364px;top:948px;width:150px"><div class="date">05/08/14</div><div class="post-title">Lorem Ipsum Dolor Sit Amet, Consectetur Adipsicing.</div></div>
<div class="abs sep" style="left:302px;top:1006px;width:209px"></div>
<div class="abs" style="left:302px;top:1013px;width:209px"><div class="date" style="color:var(--green)">05/08/14</div><div class="post-title">Lorem Ipsum Dolor Sit Amet, Consectetur Adipsicing Elit..</div><p class="small" style="margin-top:4px">Sed do eiusmod tempor incididunt ut labore et dolore magna aliqua.</p></div>
<div class="abs sep" style="left:302px;top:1090px;width:209px"></div>
<div class="abs viewall" style="left:302px;top:1096px;font-size:9.5px">→ View All</div>

<div class="abs bar green" style="left:530px;top:907px;width:208px">PennaBoschetto Tweets</div>
<div class="abs tweet" style="top:944px;height:64px">Lorem ipsum dolor sit amet, consectetur adipisicing elit, sed do eiusmod tempor incidunt !<b>#PennaBoschetto #fitness pic.example.com/aB3kL9xQ</b></div>
<div class="abs tweet" style="top:1020px;height:66px">Lorem ipsum dolor sit amet, consectetur adipisicing elit, sed do eiusmod tempor incidunt !<b>#PennaBoschetto #fitness pic.example.com/aB3kL9xQ</b></div>
<div class="abs viewall" style="left:537px;top:1096px;font-size:9.5px">→ Follow Us</div>

<footer class="abs footer">
  <div class="links"><span>Home</span><span>Scopri</span><span>Esperimenti</span><span>Ricette</span><span>Blog</span><span>Glossario</span><span>IL Progetto</span></div>
  <div class="copy">Copyrights © 2014 pennaboschetto.com - All Rights Reserved</div>
</footer>
</body>
</html>
```